Plakat für Hersteller von maßgefertigten Tischunikaten aus Massivholz
Zielgruppe
Wir sind einen Firma die sich auf die Fertigung von maßgefertigten Tischunikaten aus Massivholz spezialisiert hat. Unsere Zielgruppe sind Design affine Leute, im Alter von 35-55 Jahren
Aufgabenstellung
Wir benötigen das Design für eine Messewand mit den Maßen 443X227 cm. 5 Zentimeter rundlaufen dürfen keine Elemente mehr platziert werden. Die Messewand steht im Hintergrund von unserem Stand bei verschiedenen Designmessen
Infos die auf die Messewand müssen: Logo, Tischmanufaktur aus Stuttgart, Maßgefertigte Tischunikate (Bei der Formulierung bin ich flexibel, ihr könnt bspw. auch nur Stichworte benutzen, aber Stuttgart und maßgefertigt ist wichtig).
Die Messewand soll sehr minimalistisch gestaltet sein, bei der letzten Messewand hatten wir ein Foto von einem Tisch im Hintergrund und das sah merkwürdig aus.

```html
<!DOCTYPE html>
<html lang="de">
<head>
<meta charset="utf-8">
<title>Brandtner Manufaktur – Messewand</title>
<link rel="stylesheet" href="https://fonts.googleapis.com/css2?family=Montserrat:wght@300;400;600;700&display=swap">
<style>
  :root {
    --page: #efeeea;
    --stone: #1e1e1e;
    --band: #d9d9d9;
    --wood-dark: #9a5b24;
    --wood-light: #d6a260;
    --text-light: #dcdcdc;
    --accent: #f3dcb0;
  }
  html, body {
    margin: 0;
    width: 1200px;
    height: 1117px;
    overflow: hidden;
    background: var(--page);
  }
  .fair-wall {
    position: absolute;
    left: 20px;
    top: 262px;
    width: 1160px;
    height: 593px;
    box-shadow: 0 6px 18px rgba(0,0,0,0.18);
  }
  .fair-wall svg { display: block; width: 100%; height: 100%; }
  .headline, .brand-name, .tagline, .handle { font-family: "Montserrat", sans-serif; }
  .headline { font-weight: 700; font-size: 72px; fill: var(--text-light); }
  .headline--light { font-weight: 300; }
  .tagline { font-weight: 700; font-size: 33px; letter-spacing: 14px; fill: var(--accent); }
  .brand-name { font-weight: 400; font-size: 34px; letter-spacing: 8px; fill: var(--text-light); }
  .handle { font-weight: 300; font-size: 31px; letter-spacing: 9px; fill: var(--text-light); }
</style>
</head>
<body>
  <div class="fair-wall">
    <svg viewBox="0 0 1858 950" xmlns="http://www.w3.org/2000/svg">
      <defs>
        <linearGradient id="side-tone" x1="0" y1="0" x2="1" y2="0">
          <stop offset="0" stop-color="var(--wood-dark)"/>
          <stop offset="0.55" stop-color="var(--wood-light)"/>
          <stop offset="1" stop-color="var(--wood-dark)"/>
        </linearGradient>
      </defs>

      <rect class="stone-field" x="0" y="0" width="1858" height="950" fill="var(--stone)"/>

      <rect class="side-panel side-panel--left" x="0" y="0" width="475" height="950" fill="url(#side-tone)"
            role="img" aria-label="Olivenholz-Maserung mit stilisierter hellgrauer Tischsilhouette, linke Seite"/>
      <rect class="side-panel side-panel--right" x="1383" y="0" width="475" height="950" fill="url(#side-tone)"
            role="img" aria-label="Olivenholz-Maserung mit stilisierter hellgrauer Tischsilhouette, rechte Seite"/>

      <circle class="brand-ring" cx="929" cy="225" r="150" fill="none" stroke="var(--band)" stroke-width="14"/>
      <text class="brand-name" x="929" y="450" text-anchor="middle">BRANDTNER MANUFAKTUR</text>

      <text class="headline" x="931" y="597" text-anchor="middle">TISCHMANUFAKTUR</text>
      <text class="headline headline--light" x="931" y="675" text-anchor="middle">AUS STUTTGART</text>
      <text class="tagline" x="938" y="755" text-anchor="middle">MAẞGEFERTIGT</text>

      <rect class="handle-icon" x="652" y="832" width="46" height="46" rx="9" fill="none" stroke="var(--text-light)" stroke-width="3"/>
      <text class="handle" x="714" y="867">brandtner_manufaktur</text>
    </svg>
  </div>
</body>
</html>
```